Corporate brochure for a multinational construction company

Designing the cover pages and inside pages layout for a construction company which has operations in GCC, India etc. It has to be a very classy design. you can visit our website www.belvorant.com for more details on the company. Specific information required for the brochure design will be uploaded as needed.

Please note
1. Though the brochure will be around 80 pages, we need design of only the following
a. Cover page
b. CEOs message page
c. Introduction to sectors (Civil, Electrical, Mechanical, Infra)
d. Pages showing engineering expertise
e. Pages showing Project highlights (buildings etc)
f. Gallery pages (2 to 4 images in each page showing completed projects with a small text)
g. Key personnel (images and positions of key staff)

So design has to be done for a maximum of 7 to 10 pages. rest will be repetition.
Please use stock images with the above tip and send your designs.
g.
Updates

Project Deadline Extended
Reason: Not happy with the designs provided till now. Request all designers to once again look at the brief which is updated and submit maximum revisions. The pay is committed so we will select the best in any case. wish you all the best.

Target Market(s)

International - Current operations in the GCC, India, Srilanka

Industry/Entity Type

Construction Company

Font styles to use
Serif
Sans Serif

Requirements
Must have
• 1. A great front cover design - this may run to the back cover also
• 2. Inside page layout - to have a common theme but different styling as required
• 3. More of images and less of text - can use full page, half page or quarter page images.
• 4. Different styling and sizes for fonts for better effect.
Nice to have
• 1. A4 landscape is what we have in mind. The size can be slightly reduced so that the 80 page brochure can fit into an A4 envelope

```html
<!DOCTYPE html>
<html lang="en">
<head>
<meta charset="utf-8">
<title>Belvorant Brochure Spreads</title>
<link rel="stylesheet" href="https://fonts.googleapis.com/css2?family=Open+Sans:wght@400;600;700&family=Arimo:wght@400;700&display=swap">
<style>
  :root {
    --page-bg: #ffffff;
    --sage: #6a8c65;
    --sand: #cbb06a;
    --tab-gold: #c9ab66;
    --name-gold: #cfae5e;
    --text-light: #ffffff;
    --photo-light: #fbf8e6;
    --photo-mid: #ece6d0;
    --photo-low: #b9b2a0;
    --photo-dark: #8d8678;
  }
  * { box-sizing: border-box; margin: 0; padding: 0; }
  html, body { width: 1200px; height: 900px; overflow: hidden; background: var(--page-bg); }
  body { position: relative; font-family: "Open Sans", Arial, sans-serif; color: var(--text-light); }

  .spread { position: absolute; left: 50px; width: 1081px; height: 382px; display: flex; }
  .spread--message { top: 52px; background: var(--sage); }
  .spread--sectors { top: 458px; }
  .page { position: relative; width: 540.5px; height: 100%; }
  .spread--message .page--left { border-right: 1px solid rgba(255,255,255,0.25); }

  .portrait { position: absolute; left: 215px; top: 127px; width: 109px; height: 127px; background: #fff; }
  .ceo-name { position: absolute; left: 170px; top: 264px; width: 200px; text-align: center; color: var(--name-gold); font-family: "Arimo", Arial, sans-serif; font-size: 6px; font-weight: 700; line-height: 1.2; }
  .ceo-name span { display: block; font-weight: 400; font-size: 5px; }

  .title-tab { position: absolute; left: 0; top: 139px; width: 177px; height: 103px; }
  .title-tab h1 { position: absolute; left: 36px; top: 28px; font-size: 17.5px; font-weight: 400; line-height: 22px; letter-spacing: 0.2px; }
  .title-tab h1 small { font-size: 13px; }

  .message-text { position: absolute; left: 203px; top: 105px; width: 302px; font-family: "Arimo", Arial, sans-serif; font-size: 5.6px; line-height: 7.7px; text-align: justify; }
  .message-text p + p { margin-top: 5px; }

  .page--sectors { background: var(--sand); }
  .sector { position: absolute; width: 180px; }
  .sector h2 { font-size: 11.5px; font-weight: 400; line-height: 14.5px; letter-spacing: 0.2px; margin-bottom: 6px; }
  .sector ul { list-style: none; font-family: "Arimo", Arial, sans-serif; font-size: 5.8px; line-height: 10.6px; }
  .sector li::before { content: "•"; margin-right: 4px; }
  .sector p { font-family: "Arimo", Arial, sans-serif; font-size: 5.8px; line-height: 7.9px; width: 172px; }
  .sector--civil { left: 98px; top: 65px; }
  .sector--electrical { left: 269px; top: 65px; }
  .sector--mechanical { left: 98px; top: 189px; }
  .sector--infra { left: 269px; top: 189px; }

  .site-photo { background: linear-gradient(180deg, var(--photo-light) 0%, var(--photo-light) 42%, var(--photo-mid) 62%, var(--photo-low) 82%, var(--photo-dark) 100%); }
</style>
</head>
<body>
  <section class="spread spread--message">
    <div class="page page--left">
      <div class="portrait" role="img" aria-label="Portrait photo of the CEO"></div>
      <p class="ceo-name">Dr. Martin Keller<span>CEO</span></p>
    </div>
    <div class="page page--right">
      <div class="title-tab">
        <svg width="177" height="103" viewBox="0 0 177 103" aria-hidden="true">
          <polygon points="0,0 177,0 155,40 155,103 0,103" fill="var(--tab-gold)"/>
        </svg>
        <h1>CEO<small>'s</small><br>MESSAGE</h1>
      </div>
      <div class="message-text">
        <p>A Partnership Construct From humble beginnings with consistent hard work, dedication and an eye for the future, Belvorant has been transformed into an award-winning, nationally recognized integrated engineering construction services firm. We pride ourselves on being a home-grown Omani firm but imbued with an ambition to eventually expand across the Middle East and the Indian Subcontinent.</p>
        <p>Our forte lies in delivering end-to-end solutions that respond to our customers' needs. Belvorant's integrated, cross-discipline approach ensures that our clients benefit not only from the services we provide to them, but also from the full range of our expertise. We bring to the table unmatched competencies in civil, mechanical and electricity engineering, backed by top-flight EPC and project management support.</p>
        <p>But, more than our extensive portfolio, what truly sets us apart from our competition is our people. Their dedication to providing world-class service to our clients, capacity for innovation and problem solving, and unwavering commitment to improving the construction industry we serve, not only make Belvorant a great place to work, but a company with which our clients want to work.</p>
        <p>As one of Oman's most established contractors, Belvorant's vision is rooted in a desire to partner alongside the government of His Majesty the Sultan in developing the nation's infrastructure and driving its modernization. Central to this vision is also our commitment to providing rewarding careers to young Omani men and women drawn especially from the communities and locations in which we operate. By working hand in hand with the government authorities, our goal is to help crystallize the developmental aspirations of Oman for the ultimate benefit of its people.</p>
      </div>
    </div>
  </section>

  <section class="spread spread--sectors">
    <div class="page page--sectors">
      <div class="sector sector--civil">
        <h2>CIVIL<br>ENGINEERING</h2>
        <ul><li>Foundations &amp; Structures</li><li>Architecture &amp; Interior Design</li><li>Structural Cladding &amp;Glazing</li><li>Steel Structures, Hi and Finishes</li></ul>
      </div>
      <div class="sector sector--electrical">
        <h2>ELECTRICAL<br>ENGINEERING</h2>
        <ul><li>Generation</li><li>Distribution</li><li>IT &amp; Data Centers</li><li>Utilities</li></ul>
      </div>
      <div class="sector sector--mechanical">
        <h2>MECHANICAL<br>ENGINEERING</h2>
        <ul><li>HVAC</li><li>STPs</li><li>Utilities</li></ul>
      </div>
      <div class="sector sector--infra">
        <h2>INFRASTRUCTURE<br>ENGINEERING</h2>
        <p>Belvorant has delivered numerous infrastructure projects across Oman over the past three decades building roads, bridges, pipelines and canals. Our presence extends from Musandam in the north to Salalah in the south and Masirah Island in the east to Ibri in the west.</p>
      </div>
    </div>
    <div class="page site-photo" role="img" aria-label="Photo of an engineer in hard hat and safety vest checking a clipboard on a construction site with cranes behind"></div>
  </section>
</body>
</html>
```